Brisk Motion Studio Chinese New Year Special

We want to attract new people to our gym

I will be looking for a graphic that we can use for posting on our FB and making flyers. We are a coin operated fitness center, much like a laundromat without the washers and dryers, but treadmills instead.

-I want to make it clear that we are not a regular gym that we don't have contracts(its pay as you go) and we don't have sales people to hassle anyone.

-The main theme is Chinese New Years (so Chinese New Year colors and designs appropriate).

-If we use people exercising I would like them to look Chinese and be on a piece of cardio equipment, but not weights, we do not have weights.

-Our colors are yellow and black.

-we'd like to draw likes to our FB page

-call to action is buy 40 tokens and get 10 free. Must send shipping address to our FB message service. Then we will send tokens COD. FB:BRISKMOTIONSTUDIO

-In the end you will need to change all of the text to Chinese. I will give you the text to replace what you create.
Updates

Target Market(s)

Target to women interested in fitness, weight loss, wellness, etc. between the ages of 18 - 50. We accept men too, but I would like the over all appeal to women. Safe, gentle, warm, inviting, etc... since we are 24 hours, I want this image.

Industry/Entity Type

Fitness

Font styles to use
Sans Serif

Colors
fbee3f
262626
ec1f27

Requirements
Must have
• Like us in FB
• Yellow and black
• Chinese New Year Theme
• Buy 40 tokens get 10 free + special coin purse (I'll add a picture). Send FB message to order.
• Club locations - I'll send a map.
• Phone number
• Our logo and name Brisk Motion Studio
• Tag line "We are not a normal gym"
Nice to have
• Your personal touch, give our message a unifying theme and make the design warm, comfortable, and safe.
Should not have
• Some of the photos are just for example. I would like this project to have a different look from previous designs, but provide all of the correct information.

```html
<!DOCTYPE html>
<html lang="en">
<head>
<meta charset="utf-8">
<title>Brisk Motion Studio – Chinese New Year Flyer</title>
<link rel="stylesheet" href="https://fonts.googleapis.com/css2?family=Anton&family=Lato:wght@400;700;900&family=Lobster&display=swap">
<style>
  :root {
    --page-bg: #e4e4e4;
    --red-deep: #8e0a0c;
    --red: #c8161d;
    --red-bright: #ec1f27;
    --yellow: #fbee3f;
    --yellow-strong: #f6df12;
    --gold: #e8b90f;
    --black: #262626;
    --white: #ffffff;
  }
  * { box-sizing: border-box; margin: 0; padding: 0; }
  html, body { width: 1200px; height: 1200px; overflow: hidden; background: var(--page-bg); }
  .stage { position: relative; width: 1200px; height: 1200px; }
  .flyer {
    position: absolute; left: 160px; top: 30px;
    width: 987px; height: 1278px;
    transform: scale(0.892); transform-origin: top left;
    overflow: hidden;
    background: linear-gradient(160deg, var(--red-deep) 0%, #a80d12 45%, var(--red) 100%);
    font-family: 'Lato', sans-serif;
  }
  .shapes { position: absolute; inset: 0; }
  .abs { position: absolute; }

  .brand-name {
    left: 40px; top: 205px; width: 230px; text-align: center;
    font: 900 17px/1.2 'Lato', sans-serif; letter-spacing: 2px; color: var(--black);
  }
  .tagline {
    left: 255px; top: 212px; width: 440px; text-align: center;
    font: 42px/1.3 'Lobster', cursive; color: var(--white);
  }
  .perks { left: 58px; top: 370px; list-style: none; }
  .perk {
    display: flex; align-items: center; gap: 24px; height: 84px;
    font: 52px/1 'Anton', sans-serif; color: var(--white); letter-spacing: 1px;
  }
  .perk svg { width: 58px; height: 56px; flex: none; }
  .body-copy { left: 54px; top: 643px; font-size: 23.5px; line-height: 29px; color: var(--white); }
  .body-caps { left: 54px; top: 800px; font-size: 26px; line-height: 29px; color: var(--white); text-transform: uppercase; }
  .phone { left: 56px; top: 900px; display: flex; align-items: center; gap: 22px; }
  .phone svg { width: 28px; height: 50px; }
  .phone-number { font: 58px/1 'Anton', sans-serif; color: var(--white); letter-spacing: 1px; }

  .offer { left: 510px; top: 780px; width: 360px; text-align: center; }
  .offer-head { font: 52px/1 'Anton', sans-serif; color: var(--yellow); }
  .offer-head.big { font-size: 56px; margin-top: 2px; }
  .offer-rule { width: 260px; height: 2px; background: var(--white); margin: 12px auto 14px; }
  .offer-sub { font-size: 31px; line-height: 32px; color: var(--white); }

  .map-label { left: 315px; top: 1078px; width: 400px; text-align: center; color: var(--black); }
  .map-label .small { font: 42px/1 'Anton', sans-serif; letter-spacing: 1px; }
  .map-label .large { font: 74px/1 'Anton', sans-serif; margin-top: 8px; }

  .social { left: 68px; top: 1078px; }
  .social-lead { font: 700 34px/1 'Lato', sans-serif; color: var(--black); }
  .social-handle { display: flex; align-items: center; gap: 14px; margin-top: 26px;
    font: 700 24px/1 'Lato', sans-serif; color: var(--black); }
  .social-dot { width: 56px; height: 56px; border-radius: 50%; background: var(--black); }
</style>
</head>
<body>
<div class="stage">
  <main class="flyer">
    <svg class="shapes" width="987" height="1278" viewBox="0 0 987 1278">
      <defs>
        <radialGradient id="lanternGlow" cx="0.72" cy="0.35" r="0.7">
          <stop offset="0" stop-color="#f0582a"/>
          <stop offset="0.35" stop-color="#d82a1e"/>
          <stop offset="1" stop-color="#a80d12" stop-opacity="0"/>
        </radialGradient>
        <linearGradient id="gymPhoto" x1="0" y1="0" x2="1" y2="1">
          <stop offset="0" stop-color="#6f9b8f"/>
          <stop offset="0.5" stop-color="#3e5a57"/>
          <stop offset="1" stop-color="#1d2a2c"/>
        </linearGradient>
      </defs>
      <rect class="lantern-photo" x="440" y="0" width="547" height="900" fill="url(#lanternGlow)" role="img" aria-label="Red Chinese New Year lantern with gold tassels and ornamental pattern"/>
      <rect class="yellow-band" x="0" y="1028" width="987" height="250" fill="var(--yellow-strong)" role="img" aria-label="Yellow-tinted gym equipment background"/>
      <path class="logo-panel" d="M0 0 H280 L345 65 Q362 82 345 99 L148 300 Q130 318 112 300 L0 190 Z" fill="var(--white)"/>
      <circle class="logo-dot" cx="155" cy="150" r="48" fill="var(--black)"/>
      <line x1="270" y1="212" x2="688" y2="212" stroke="var(--white)" stroke-width="2"/>
      <line x1="190" y1="273" x2="610" y2="273" stroke="var(--white)" stroke-width="2"/>
      <rect class="map-diamond" x="330" y="965" width="370" height="370" rx="28" transform="rotate(45 515 1150)" fill="var(--white)"/>
      <rect class="corner-diamond" x="915" y="730" width="120" height="120" rx="14" transform="rotate(45 975 790)" fill="var(--white)"/>
      <rect class="accent-diamond" x="805" y="1125" width="110" height="110" rx="10" transform="rotate(45 860 1180)" fill="var(--red-bright)"/>
      <rect class="gym-photo" x="790" y="915" width="250" height="250" rx="24" transform="rotate(45 915 1040)" fill="url(#gymPhoto)" role="img" aria-label="Woman exercising on a treadmill in the gym"/>
      <rect class="offer-diamond" x="545" y="751" width="290" height="290" rx="26" transform="rotate(45 690 896)" fill="var(--black)"/>
    </svg>

    <div class="abs brand-name">BRISK MOTION STUDIO</div>
    <div class="abs tagline">We are not a normal gym</div>

    <ul class="abs perks">
      <li class="perk"><svg viewBox="0 0 58 56"><rect x="3" y="10" width="42" height="42" fill="none" stroke="var(--gold)" stroke-width="5"/><path d="M13 28 L24 40 L54 6" fill="none" stroke="var(--gold)" stroke-width="6"/></svg>NO SALES PEOPLE</li>
      <li class="perk"><svg viewBox="0 0 58 56"><rect x="3" y="10" width="42" height="42" fill="none" stroke="var(--gold)" stroke-width="5"/><path d="M13 28 L24 40 L54 6" fill="none" stroke="var(--gold)" stroke-width="6"/></svg>NO CONTRACTS</li>
      <li class="perk"><svg viewBox="0 0 58 56"><rect x="3" y="10" width="42" height="42" fill="none" stroke="var(--gold)" stroke-width="5"/><path d="M13 28 L24 40 L54 6" fill="none" stroke="var(--gold)" stroke-width="6"/></svg>NO HASSLE</li>
    </ul>

    <p class="abs body-copy">Lorem Ipsum is simply dummy text<br>of the printing and typesetting industry.<br>Lorem Ipsum has been the industry's<br>standard dummy</p>
    <p class="abs body-caps">Lorem Ipsum is simply dummy<br>text of the printing and types.</p>

    <div class="abs phone">
      <svg viewBox="0 0 28 50"><rect x="2" y="2" width="24" height="46" rx="4" fill="none" stroke="var(--gold)" stroke-width="4"/><line x1="10" y1="42" x2="18" y2="42" stroke="var(--gold)" stroke-width="3"/></svg>
      <span class="phone-number">0980246135</span>
    </div>

    <div class="abs offer">
      <div class="offer-head">BUY</div>
      <div class="offer-head big">40 TOKENS</div>
      <div class="offer-rule"></div>
      <div class="offer-sub">GET 10 FREE +<br>SPECIAL COIN<br>PURSE</div>
    </div>

    <div class="abs map-label">
      <div class="small">CLUB LOCATION</div>
      <div class="large">MAP</div>
    </div>

    <div class="abs social">
      <div class="social-lead">Like us in</div>
      <div class="social-handle"><span class="social-dot"></span>Friendbook</div>
    </div>
  </main>
</div>
</body>
</html>
```